Velmar Industrial Coatings

We are looking to improve our business cards. Our company installs industrial floor and wall coatings in industrial, chemical and food processing plants.
Our coatings which consist of epoxy, urethane, and vinyl esters provide chemical and abrasion resistant surface with non-skid properties that are easy to clean.

Target Market(s)

food manufacturing, chemical plants, breweries and wineries, warehouses, clean room floors.

Industry/Entity Type

Construction

Contact Information for Business Card

improved current logo.

Colors

Designer to choose colors to be used in the design.

Requirements
Must have
• the information from uploaded file
Nice to have
• "We'll be outstanding on your floors."

```html
<!DOCTYPE html>
<html lang="en">
<head>
<meta charset="utf-8">
<title>Velmar Industrial Coatings — Business Card</title>
<link rel="stylesheet" href="https://fonts.googleapis.com/css2?family=Roboto:wght@400;500&display=swap">
<style>
  :root {
    --card-bg: #f4f4f4;
    --ink: #1c1c1c;
    --ink-soft: #4a4a4a;
    --band: #2e2e2e;
    --band-text: #f4f4f4;
    --accent: #e0a526;
  }
  html, body {
    margin: 0;
    padding: 0;
    overflow: hidden;
    background: var(--card-bg);
  }
  .card {
    position: relative;
    width: 1200px;
    height: 696px;
    background: var(--card-bg);
    color: var(--ink);
    font-family: "Roboto", sans-serif;
    overflow: hidden;
  }
  .card-header {
    position: absolute;
    top: 80px;
    left: 0;
    width: 1200px;
    text-align: center;
  }
  .company-name {
    margin: 0;
    font-size: 56px;
    font-weight: 400;
    line-height: 1;
    letter-spacing: 1px;
  }
  .contact-person {
    margin-top: 34px;
    font-size: 28px;
    font-weight: 500;
    letter-spacing: 3px;
    line-height: 1;
  }
  .contact-direct {
    margin-top: 18px;
    font-size: 30px;
    line-height: 1.4;
  }
  .contact-direct .divider {
    display: inline-block;
    width: 8px;
    height: 8px;
    margin: 0 18px;
    vertical-align: middle;
    background: var(--accent);
  }
  .detail-block {
    position: absolute;
    top: 340px;
    font-size: 30px;
    line-height: 44px;
  }
  .mailing-address { left: 143px; }
  .phone-list {
    right: 125px;
    display: grid;
    grid-template-columns: auto auto;
    column-gap: 16px;
  }
  .phone-list .label {
    color: var(--ink-soft);
    text-align: right;
  }
  .footer-band {
    position: absolute;
    left: 0;
    top: 605px;
    width: 1200px;
    height: 91px;
    background: var(--band);
    border-top: 5px solid var(--accent);
    box-sizing: border-box;
    display: flex;
    align-items: center;
    justify-content: center;
  }
  .tagline {
    margin: 0;
    color: var(--band-text);
    font-size: 28px;
    letter-spacing: 1px;
  }
</style>
</head>
<body>
  <main class="card">
    <header class="card-header">
      <h1 class="company-name">VELMAR INDUSTRIAL COATINGS INC</h1>
      <div class="contact-person">NEIL HARPER</div>
      <div class="contact-direct">1-800-555-0148<span class="divider"></span>neil@velmarfloors.com</div>
    </header>

    <address class="detail-block mailing-address" style="font-style: normal;">
      Velmar Inc.<br>
      PO Box 42<br>
      Marlow, WA 98500
    </address>

    <div class="detail-block phone-list">
      <span class="label">Office</span><span>(360) 555-0192</span>
      <span class="label">Cell</span><span>(360) 555-0174</span>
      <span class="label">Fax</span><span>(360) 555-0139</span>
    </div>

    <footer class="footer-band">
      <p class="tagline">We'll be outstanding on your floors.</p>
    </footer>
  </main>
</body>
</html>
```